Ad for regional magazine for startup "Varumo"

We need a small ad for a small German regional magazine for our startup company Varumo which provides on-premise service for all kind of electronic problems.

We also need the Indesign files to be able to make minor changes (e.g. the phone number) in the future.

An example ad that we used before (for another region with another phone number) is attached.

Industry/Entity Type

Technical Service

Requirements
Must have
• Needed contents:
• "Elektronik-Problem?" (Electronic problem?)
• "Ihr Media-Pannenhelfer kommt" (Your media helper comes)
• "TV, Video, Telefon, Smartphone, Internet, Computer"
• "Terminbuchung: 07041-3926518" (booking)
• "Soforthilfe - auch abends und am Wochenende" (immediate help - also in the evenings and at the weekend)
• "www.varumo.de"
• logo
• picture
• Size: 90mm (width) x 50-70mm (height)
• Font & colors: see attachment

```html
<!DOCTYPE html>
<html lang="de">
<head>
<meta charset="utf-8">
<title>Varumo – Anzeigenvarianten</title>
<link rel="stylesheet" href="https://fonts.googleapis.com/css2?family=Open+Sans:wdth,wght@75..100,400..700&display=swap">
<style>
  :root{
    --green:#9fc33c;
    --green-band:rgba(159,195,60,.85);
    --ink:#4b5055;
    --ink-dark:#3f4448;
    --white:#ffffff;
    --label:#8a8a8a;
    --frame:#c9c9c9;
    --ic-teal:#38b0c6;
    --ic-yellow:#f2c230;
    --ic-navy:#24507b;
    --ic-grey:#7d8287;
    --ic-orange:#f0683a;
    --ic-green:#9fc33c;
  }
  *{box-sizing:border-box;margin:0;padding:0}
  html,body{width:1200px;height:1028px;overflow:hidden;background:#fff}
  body{font-family:"Open Sans",Arial,sans-serif;color:var(--ink);position:relative}
  .sheet{position:absolute;inset:0;border:1px solid var(--frame)}
  .abs{position:absolute;white-space:nowrap}
  .center{text-align:center}
  .condensed{font-stretch:75%}
  .size-label{position:absolute;font-family:Arial,Helvetica,sans-serif;font-size:21px;color:var(--label);text-align:center;white-space:nowrap}

  .icon-row{position:absolute;display:flex}
  .icon{border-radius:50%;display:flex;align-items:center;justify-content:center;flex:none}
  .icon svg{width:58%;height:58%}
  .tv{background:var(--ic-teal)} .video{background:var(--ic-yellow)} .phone{background:var(--ic-navy)}
  .mobile{background:var(--ic-grey)} .net{background:var(--ic-orange)} .pc{background:var(--ic-green)}

  .brand{font-weight:700;color:var(--ink-dark);letter-spacing:.5px}

  /* Ad 90x50 */
  .ad-small{position:absolute;left:60px;top:40px;width:638px;height:353px;background:var(--green)}
  .ad-small .panel{position:absolute;left:21px;top:21px;width:598px;height:280px;background:var(--white);border-radius:13px}

  /* Ad 50x70 */
  .ad-tall{position:absolute;left:793px;top:42px;width:355px;height:498px;background:var(--white);border:1px solid var(--ink)}
  .photo{position:absolute;background:linear-gradient(100deg,#c9c6c0 0%,#e9e6e0 35%,#d8d2c8 60%,#f1efeb 85%,#c7c2b6 100%)}
  .band{position:absolute;background:var(--green-band);color:var(--white)}

  /* Ad 90x70 */
  .ad-wide{position:absolute;left:60px;top:469px;width:639px;height:498px;background:var(--white);border:1px solid var(--frame)}
  .ad-wide .green-top{position:absolute;left:0;top:0;width:100%;height:301px;background:var(--green)}
</style>
</head>
<body>
<svg width="0" height="0" style="position:absolute" aria-hidden="true">
  <defs>
    <symbol id="g-tv" viewBox="0 0 24 24"><path d="M9 3l3 3 3-3" stroke="#fff" stroke-width="1.5" fill="none"/><rect x="3" y="6.5" width="18" height="12.5" rx="1.5" fill="none" stroke="#fff" stroke-width="1.8"/><rect x="5.5" y="9" width="10" height="7.5" fill="#fff"/><rect x="6" y="19" width="12" height="1.6" fill="#fff"/></symbol>
    <symbol id="g-video" viewBox="0 0 24 24"><rect x="2.5" y="5" width="19" height="14" rx="1" fill="none" stroke="#fff" stroke-width="1.8"/><path d="M2.5 8h19M2.5 16h19" stroke="#fff" stroke-width="1.2"/><path d="M10 9.5v5l4.3-2.5z" fill="#fff"/></symbol>
    <symbol id="g-phone" viewBox="0 0 24 24"><path d="M2.5 9.5C7 4.5 17 4.5 21.5 9.5l-1.8 2.3-3.3-1.2V8.5H7.6v2.1l-3.3 1.2z" fill="#fff"/><path d="M6.5 12.5h11l2 8h-15z" fill="#fff"/><circle cx="12" cy="16.3" r="2.6" fill="none" stroke="#24507b" stroke-width="1.3"/><circle cx="12" cy="16.3" r=".9" fill="#24507b"/></symbol>
    <symbol id="g-mobile" viewBox="0 0 24 24"><rect x="6" y="2.5" width="11" height="19" rx="1.8" fill="none" stroke="#fff" stroke-width="1.8"/><rect x="8" y="5" width="7" height="12" fill="#fff"/><circle cx="11.5" cy="19.3" r=".9" fill="#fff"/><path d="M12.5 11.5v5.5l-1.3-1v3.5h6v-4.5l-3.2-1.2v-2.3z" fill="#7d8287" stroke="#fff" stroke-width="1"/></symbol>
    <symbol id="g-net" viewBox="0 0 24 24"><circle cx="12" cy="7.5" r="1.7" fill="#fff"/><path d="M8.6 4.4a4.5 4.5 0 000 6.2M15.4 4.4a4.5 4.5 0 010 6.2M6.2 2.4a8 8 0 000 10.2M17.8 2.4a8 8 0 010 10.2" stroke="#fff" stroke-width="1.4" fill="none"/><path d="M12 9.5L7.5 22M12 9.5l4.5 13M9.4 17h5.2" stroke="#fff" stroke-width="1.8" fill="none"/></symbol>
    <symbol id="g-pc" viewBox="0 0 24 24"><rect x="2" y="5" width="13" height="10" rx=".8" fill="#fff"/><rect x="3.5" y="6.5" width="10" height="7" fill="#9fc33c"/><path d="M7 15h3v2.5H7zM4.5 18h8v1.5h-8z" fill="#fff"/><rect x="16.5" y="4" width="5" height="15.5" rx=".8" fill="#fff"/><path d="M17.8 6.5h2.4M17.8 8.5h2.4" stroke="#9fc33c" stroke-width="1"/></symbol>
  </defs>
</svg>

<div class="sheet">

  <!-- 90 x 50 -->
  <section class="ad-small">
    <div class="panel">
      <div class="abs center" style="left:0;width:598px;top:0;font-size:46px;font-weight:700;color:var(--ink)">Elektronik-Problem?</div>
      <div class="abs center" style="left:0;width:598px;top:63px;font-size:25px;color:var(--green)">Ihr Media-Pannenhelfer kommt</div>
      <div class="icon-row" style="left:81px;top:96px;gap:17px">
        <div class="icon tv" style="width:58px;height:58px"><svg><use href="#g-tv"/></svg></div>
        <div class="icon video" style="width:58px;height:58px"><svg><use href="#g-video"/></svg></div>
        <div class="icon phone" style="width:58px;height:58px"><svg><use href="#g-phone"/></svg></div>
        <div class="icon mobile" style="width:58px;height:58px"><svg><use href="#g-mobile"/></svg></div>
        <div class="icon net" style="width:58px;height:58px"><svg><use href="#g-net"/></svg></div>
        <div class="icon pc" style="width:58px;height:58px"><svg><use href="#g-pc"/></svg></div>
      </div>
      <div class="abs center condensed" style="left:0;width:598px;top:163px;font-size:19px;color:var(--ink-dark)">TV, VIDEO, TELEFON, SMARTPHONE, INTERNET, COMPUTER</div>
      <div class="abs center condensed" style="left:0;width:578px;top:199px;font-size:17px;color:var(--ink-dark)">Soforthilfe - auch abends und am Wochenende</div>
      <div class="abs brand" style="left:36px;top:223px;font-size:44px;line-height:60px">Varumo</div>
      <div class="abs" style="left:299px;top:239px;font-size:26px;letter-spacing:5px;color:var(--ink-dark)">www.varumo.de</div>
    </div>
    <div class="abs" style="left:30px;top:301px;font-size:36px;font-weight:700;color:var(--white);letter-spacing:.3px">Terminbuchung: 07041-3926518</div>
  </section>
  <div class="size-label" style="left:60px;width:638px;top:406px">90mm (width) x 50 hight</div>

  <!-- 50 x 70 -->
  <section class="ad-tall">
    <div class="abs center" style="left:0;width:353px;top:34px;font-size:30px;font-weight:700;color:var(--green)">Elektronik-Problem?</div>
    <div class="abs center" style="left:0;width:353px;top:66px;font-size:18px;color:var(--ink-dark)">Ihr Media-Pannenhelfer kommt</div>
    <div class="photo" style="left:0;top:91px;width:353px;height:235px" role="img" aria-label="Foto: Servicetechniker erklärt einem älteren Kunden am Tisch ein Tablet"></div>
    <div class="band condensed center" style="left:0;top:285px;width:353px;height:41px;font-size:16px;line-height:19px;padding-top:2px">TV, VIDEO, TELEFON, SMARTPHONE,<br>INTERNET, COMPUTER AND MANY MORE...</div>
    <div class="icon-row" style="left:3px;top:332px;gap:14.5px">
      <div class="icon tv" style="width:46px;height:46px"><svg><use href="#g-tv"/></svg></div>
      <div class="icon video" style="width:46px;height:46px"><svg><use href="#g-video"/></svg></div>
      <div class="icon phone" style="width:46px;height:46px"><svg><use href="#g-phone"/></svg></div>
      <div class="icon mobile" style="width:46px;height:46px"><svg><use href="#g-mobile"/></svg></div>
      <div class="icon net" style="width:46px;height:46px"><svg><use href="#g-net"/></svg></div>
      <div class="icon pc" style="width:46px;height:46px"><svg><use href="#g-pc"/></svg></div>
    </div>
    <div class="abs center condensed" style="left:0;width:353px;top:388px;font-size:16px;color:var(--ink-dark)">Soforthilfe - auch abends und am Wochenende</div>
    <svg class="abs" style="left:8px;top:414px" width="338" height="10" aria-hidden="true"><path d="M0 6.5H240l4-4 4 4H338" stroke="#4b5055" stroke-width="1" stroke-dasharray="2 2" fill="none"/></svg>
    <div class="abs center" style="left:0;width:353px;top:425px;font-size:19px;font-weight:700;color:var(--ink-dark)">Terminbuchung: 07041-3926518</div>
    <div class="abs" style="left:13px;top:460px;font-size:19px;font-weight:700;color:var(--ink-dark)">www.varumo.de</div>
    <div class="abs brand" style="left:193px;top:456px;font-size:25px">Varumo</div>
  </section>
  <div class="size-label" style="left:793px;width:355px;top:561px">50 mm (width) x 70 hight</div>

  <!-- 90 x 70 -->
  <section class="ad-wide">
    <div class="green-top"></div>
    <div class="abs center" style="left:0;width:637px;top:9px;font-size:44px;font-weight:700;color:var(--white)">Elektronik-Problem?</div>
    <div class="abs center" style="left:0;width:637px;top:55px;font-size:25px;color:var(--white)">Ihr Media-Pannenhelfer kommt</div>
    <div class="photo" style="left:39px;top:85px;width:559px;height:258px" role="img" aria-label="Foto: Servicetechniker zeigt einem älteren Kunden am Esstisch ein Tablet"></div>
    <div class="icon-row" style="left:101px;top:281px;gap:17px">
      <div class="icon tv" style="width:58px;height:58px"><svg><use href="#g-tv"/></svg></div>
      <div class="icon video" style="width:58px;height:58px"><svg><use href="#g-video"/></svg></div>
      <div class="icon phone" style="width:58px;height:58px"><svg><use href="#g-phone"/></svg></div>
      <div class="icon mobile" style="width:58px;height:58px"><svg><use href="#g-mobile"/></svg></div>
      <div class="icon net" style="width:58px;height:58px"><svg><use href="#g-net"/></svg></div>
      <div class="icon pc" style="width:58px;height:58px"><svg><use href="#g-pc"/></svg></div>
    </div>
    <div class="band condensed center" style="left:0;top:343px;width:637px;height:40px;background:var(--green);font-size:17px;line-height:40px">TV, VIDEO, TELEFON, SMARTPHONE, INTERNET, COMPUTER AND MANY MORE...</div>
    <div class="abs" style="left:38px;top:397px;font-size:24px;font-weight:700;line-height:29px;color:var(--ink-dark)">Terminbuchung:<br>07041-3926518<br>www.varumo.de</div>
    <div class="abs" style="right:38px;top:392px;font-size:20px;line-height:26px;text-align:right;color:var(--ink-dark)">Soforthilfe - auch abends<br>und am Wochenende</div>
    <div class="abs brand" style="right:32px;top:438px;font-size:40px;line-height:48px">Varumo</div>
    <div class="abs" style="left:0;top:488px;width:351px;height:8px;background:var(--ink)"></div>
    <div class="abs" style="left:351px;top:488px;width:286px;height:8px;background:var(--green)"></div>
  </section>
  <div class="size-label" style="left:60px;width:638px;top:983px">90mm (width) x 70 hight</div>

</div>
</body>
</html>
```